I need a business card for a residential and apartment building development company. The card should be very high end prestige. Possibly a black card with a foil?? The card should be classical and simple yet very high end. The company currently does not have a logo so we can use graphical elements that suggest a building developement company.

Darvane Holdings LLC
917-555-0148 phone
877-555-0193 fax
Teodor.Mavrakis@fernmail.example
General Construction Real Estate Investments and Development
47 Halbrook Terrace
North 4C
Bronx, NY 10298

```html
<!DOCTYPE html>
<html lang="en">
<head>
<meta charset="utf-8">
<title>Darvane Holdings LLC – Business Card</title>
<link rel="stylesheet" href="https://fonts.googleapis.com/css2?family=PT+Sans:wght@400;700&display=swap">
<style>
  :root {
    --page-bg: #ffffff;
    --card-navy: #0f1340;
    --card-glow: #27338f;
    --card-edge: #0a0d2e;
    --gold: #f7d117;
    --ink-light: #ffffff;
    --shadow: rgba(0, 0, 0, 0.35);
  }
  * { box-sizing: border-box; margin: 0; padding: 0; }
  html, body {
    width: 1200px;
    height: 1000px;
    overflow: hidden;
    background: var(--page-bg);
  }
  .canvas {
    position: relative;
    width: 1200px;
    height: 1000px;
  }
  .business-card {
    position: absolute;
    left: 150px;
    top: 230px;
    width: 900px;
    height: 540px;
    background: radial-gradient(ellipse 60% 55% at 50% 38%, var(--card-glow) 0%, var(--card-navy) 62%, var(--card-edge) 100%);
    box-shadow: 10px 12px 14px var(--shadow);
    display: flex;
    flex-direction: column;
    align-items: center;
    justify-content: center;
    font-family: "PT Sans", Arial, sans-serif;
    color: var(--ink-light);
    text-align: center;
  }
  .brand {
    display: flex;
    align-items: center;
    gap: 16px;
    margin-bottom: 10px;
  }
  .brand-mark {
    width: 30px;
    height: 30px;
    background: var(--gold);
  }
  .brand-name {
    font-size: 44px;
    font-weight: 700;
    letter-spacing: 0.5px;
    color: var(--ink-light);
    text-transform: uppercase;
    line-height: 1;
  }
  .address {
    font-size: 21px;
    line-height: 1.25;
  }
  .address strong { font-weight: 700; }
  .contact-line {
    font-size: 18px;
    line-height: 1.4;
    margin-bottom: 46px;
  }
  .contact-line .label { font-weight: 700; }
  .contact-line .sep { margin: 0 8px; }
  .tagline {
    font-size: 22px;
    font-weight: 700;
    color: var(--gold);
  }
</style>
</head>
<body>
  <main class="canvas">
    <section class="business-card">
      <div class="brand">
        <span class="brand-mark" aria-hidden="true"></span>
        <h1 class="brand-name">Darvane Holdings LLC</h1>
      </div>
      <p class="address"><strong>47 Halbrook Terrace</strong> • North 4C • Bronx, NY 10298</p>
      <p class="contact-line">
        <span class="label">tel:</span> 917-555-0148<span class="sep">/</span><span class="label">fax:</span> 877-555-0193<span class="sep">/</span><span class="label">email:</span> Teodor.Mavrakis@fernmail.example
      </p>
      <p class="tagline">General Construction Real Estate Investments and Development</p>
    </section>
  </main>
</body>
</html>
```